Corvella Santoro Winery 2023 Label

We are just about to bottle our very first Napa Valley Cabernet Sauvignon and need label ideas

Target Market(s)

Cab drinkers who like Napa California Cabs

Industry/Entity Type

Wine Making

Logo Text

Corvella Santoro 2023 Napa Estate Grown Cabernet Sauvignon

Requirements
Must have
• Winery Name, year of vintage and Napa Estate Cab
Nice to have
• If using the initials C and S use gold letters on black or red background

```html
<!DOCTYPE html>
<html lang="en">
<head>
<meta charset="utf-8">
<title>Corvella Santoro 2023 Cabernet Sauvignon Label</title>
<link rel="stylesheet" href="https://fonts.googleapis.com/css2?family=Cinzel:wght@400;600;700&family=Cormorant+SC:wght@600&display=swap">
<style>
  :root {
    --paper: #efe9dc;
    --paper-shade: #e6dfcf;
    --ink: #1d1a17;
    --frame: #4a4038;
    --gold-dark: #9a7336;
    --gold: #c9a25f;
    --gold-light: #e3c68e;
    --burgundy: #4a1526;
  }
  * { margin: 0; padding: 0; box-sizing: border-box; }
  html, body { width: 1200px; height: 900px; overflow: hidden; background: var(--paper); }
  .label {
    position: relative;
    width: 1200px;
    height: 900px;
    background: radial-gradient(ellipse at center, var(--paper) 55%, var(--paper-shade) 100%);
    font-family: "Cinzel", serif;
    color: var(--ink);
  }
  .frame { position: absolute; inset: 0; }
  .corner-ornament {
    position: absolute;
    width: 34px;
    height: 34px;
    background: var(--paper-shade);
    border-radius: 4px;
  }
  .corner-ornament.tl { left: 60px; top: 60px; }
  .corner-ornament.tr { right: 60px; top: 60px; }
  .corner-ornament.bl { left: 60px; bottom: 60px; }
  .corner-ornament.br { right: 60px; bottom: 60px; }

  .brand-mark {
    position: absolute;
    top: 215px;
    left: 0;
    width: 1200px;
    display: flex;
    justify-content: center;
    align-items: center;
    gap: 18px;
  }
  .brand-mark .dot {
    width: 44px;
    height: 44px;
    border-radius: 50%;
    background: var(--burgundy);
  }
  .brand-mark .name {
    font-family: "Cinzel", serif;
    font-weight: 600;
    font-size: 34px;
    letter-spacing: 2px;
    color: var(--burgundy);
  }

  .gold-band {
    position: absolute;
    top: 417px;
    height: 64px;
    display: flex;
    align-items: center;
    font-family: "Cinzel", serif;
    font-size: 19px;
    letter-spacing: 1.5px;
    color: var(--ink);
  }
  .gold-band.left {
    left: 0;
    width: 268px;
    padding-left: 34px;
    background: linear-gradient(90deg, var(--gold-dark), var(--gold) 45%, var(--gold-light) 85%, rgba(227,198,142,0));
  }
  .gold-band.right {
    right: 0;
    width: 280px;
    justify-content: flex-end;
    padding-right: 34px;
    background: linear-gradient(270deg, var(--gold-dark), var(--gold) 45%, var(--gold-light) 85%, rgba(227,198,142,0));
  }

  .wine-name {
    position: absolute;
    top: 395px;
    left: 0;
    width: 1200px;
    text-align: center;
    font-family: "Cinzel", serif;
    font-weight: 600;
    line-height: 84px;
    font-size: 82px;
    letter-spacing: 1px;
    color: var(--ink);
    text-shadow: 1px 1px 0 rgba(0,0,0,0.12);
  }
  .vintage {
    position: absolute;
    top: 592px;
    left: 0;
    width: 1200px;
    text-align: center;
    font-family: "Cinzel", serif;
    font-size: 34px;
    letter-spacing: 2px;
  }
  .varietal {
    position: absolute;
    top: 662px;
    left: 0;
    width: 1200px;
    text-align: center;
    font-family: "Cormorant SC", serif;
    font-weight: 600;
    font-size: 44px;
    line-height: 48px;
    letter-spacing: 0.5px;
  }
</style>
</head>
<body>
<main class="label">
  <svg class="frame" width="1200" height="900" viewBox="0 0 1200 900" aria-hidden="true">
    <path d="M100 58 H1100 M100 842 H1100 M58 100 V800 M1142 100 V800" stroke="var(--frame)" stroke-width="2.5" fill="none"/>
    <path d="M100 58 Q100 100 58 100 M1100 58 Q1100 100 1142 100 M100 842 Q100 800 58 800 M1100 842 Q1100 800 1142 800" stroke="var(--frame)" stroke-width="2.5" fill="none"/>
    <rect x="70" y="70" width="1060" height="760" stroke="var(--frame)" stroke-width="1.2" fill="none"/>
  </svg>
  <div class="corner-ornament tl" role="img" aria-label="Corner flourish ornament"></div>
  <div class="corner-ornament tr" role="img" aria-label="Corner flourish ornament"></div>
  <div class="corner-ornament bl" role="img" aria-label="Corner flourish ornament"></div>
  <div class="corner-ornament br" role="img" aria-label="Corner flourish ornament"></div>

  <div class="brand-mark">
    <span class="dot"></span>
    <span class="name">Corvella Santoro</span>
  </div>

  <div class="gold-band left">Estate 2023</div>
  <div class="gold-band right">Cabernet</div>

  <h1 class="wine-name">Corvella<br>Santoro</h1>
  <p class="vintage">2023</p>
  <p class="varietal">Napa Estate Grown<br>Cabernet Sauvignon</p>
</main>
</body>
</html>
```